Make attractive Packaging label for NUT BUTTERS jars

We at Briarwood Pantry are launching our own line of NUT BUTTERS. We will be serving them in GLASS JARS ready packaged. I need attractive luxurious design for glass jar and should be designed ready to print.
I have attached glass jar pictures and measurement sheet.
My company logo has been attached. Also company details can be found on our facebook page.
product will be

ALMOND BUTTER
CASHEW BUTTER
PEANUT BUTTER
HAZELNUT BUTTER.

Industry/Entity Type

Retail

```html
<!DOCTYPE html>
<html lang="en">
<head>
<meta charset="utf-8">
<title>Briarwood Pantry – Almond Butter Label</title>
<link rel="stylesheet" href="https://fonts.googleapis.com/css2?family=Bree+Serif&family=Quicksand:wght@500;700&display=swap">
<style>
  :root {
    --backdrop: #ececec;
    --label-cream: #f6f2ea;
    --label-edge: #e6dfd2;
    --cocoa: #4e3326;
    --cocoa-light: #6b4938;
    --caramel: #c89a55;
    --almond-tan: #a97a52;
    --almond-soft: #d9bfa3;
    --ink: #3a2a22;
    --white: #ffffff;
  }
  * { margin: 0; padding: 0; box-sizing: border-box; }
  html, body { width: 1200px; height: 800px; overflow: hidden; }
  body {
    background: var(--backdrop);
    display: flex;
    align-items: center;
    justify-content: center;
    font-family: "Quicksand", sans-serif;
    color: var(--ink);
  }
  .jar-label {
    position: relative;
    width: 1100px;
    height: 680px;
    background: var(--label-cream);
    border: 1px solid var(--label-edge);
    overflow: hidden;
  }
  .serving-photo {
    position: absolute;
    left: -120px;
    top: 20px;
    width: 240px;
    height: 240px;
    border-radius: 50%;
    border: 6px solid #c9dbe6;
    background: radial-gradient(circle at 60% 45%, #d6a878 0%, #a87a50 55%, #7a5337 100%);
  }
  .almond-scatter {
    position: absolute;
    border-radius: 40px;
    background: radial-gradient(ellipse at center, rgba(169,122,82,0.28) 0%, rgba(169,122,82,0.10) 55%, rgba(169,122,82,0) 80%);
  }
  .almond-scatter--left { left: 0; top: 250px; width: 200px; height: 260px; }
  .almond-scatter--right { right: 30px; top: 40px; width: 260px; height: 540px; }
  .almond-scatter--top { left: 560px; top: 20px; width: 180px; height: 60px; }
  .label-content {
    position: absolute;
    inset: 0;
    display: flex;
    flex-direction: column;
    align-items: center;
    padding-top: 70px;
  }
  .brand-name {
    font-family: "Bree Serif", serif;
    font-weight: 400;
    font-size: 84px;
    line-height: 1;
    color: var(--cocoa);
    letter-spacing: 1px;
  }
  .product-badge {
    position: relative;
    margin-top: 56px;
    width: 560px;
    height: 230px;
  }
  .product-badge svg { position: absolute; inset: 0; }
  .product-name {
    position: absolute;
    left: 40px;
    top: 38px;
    width: 420px;
    font-family: "Bree Serif", serif;
    font-size: 74px;
    line-height: 0.98;
    color: var(--white);
    text-align: center;
  }
  .contact-block {
    margin-top: 34px;
    display: flex;
    flex-direction: column;
    align-items: center;
    gap: 6px;
  }
  .contact-phone {
    font-weight: 700;
    font-size: 32px;
    color: var(--ink);
    letter-spacing: 1px;
    margin-bottom: 4px;
  }
  .contact-line {
    display: flex;
    align-items: center;
    gap: 8px;
    font-weight: 500;
    font-size: 18px;
    color: var(--ink);
  }
  .contact-icon { width: 16px; height: 16px; flex: none; }
</style>
</head>
<body>
  <main class="jar-label">
    <div class="serving-photo" role="img" aria-label="Bowl of creamy almond butter"></div>
    <div class="almond-scatter almond-scatter--left" role="img" aria-label="Scattered whole almonds"></div>
    <div class="almond-scatter almond-scatter--right" role="img" aria-label="Scattered whole almonds"></div>
    <div class="almond-scatter almond-scatter--top" role="img" aria-label="Scattered whole almonds"></div>

    <div class="label-content">
      <h1 class="brand-name">Briarwood Pantry</h1>

      <div class="product-badge">
        <svg viewBox="0 0 560 230" width="560" height="230" aria-hidden="true">
          <path d="M150 8 C 300 0, 420 40, 552 115 C 420 190, 300 230, 150 222 C 50 216, 8 175, 8 115 C 8 55, 50 14, 150 8 Z" fill="var(--cocoa)"/>
          <path d="M60 115 C 200 95, 380 95, 520 115" fill="none" stroke="var(--cocoa-light)" stroke-width="3"/>
        </svg>
        <h2 class="product-name">Almond<br>Butter</h2>
      </div>

      <div class="contact-block">
        <p class="contact-phone">+353 85 402 7719</p>
        <p class="contact-line">
          <svg class="contact-icon" viewBox="0 0 16 16" aria-hidden="true"><rect x="1" y="3" width="14" height="10" rx="1.5" fill="none" stroke="var(--caramel)" stroke-width="1.6"/><path d="M1.5 4 L8 9 L14.5 4" fill="none" stroke="var(--caramel)" stroke-width="1.6"/></svg>
          hello@briarwoodpantry.ie
        </p>
        <p class="contact-line">
          <svg class="contact-icon" viewBox="0 0 16 16" aria-hidden="true"><rect x="2" y="2" width="12" height="12" rx="2" fill="var(--cocoa)"/></svg>
          www.briarwoodpantry.ie/shop
        </p>
        <p class="contact-line">
          <svg class="contact-icon" viewBox="0 0 16 16" aria-hidden="true"><path d="M8 1 C 4.8 1, 3 3.3, 3 6 C 3 9.5, 8 15, 8 15 C 8 15, 13 9.5, 13 6 C 13 3.3, 11.2 1, 8 1 Z" fill="var(--caramel)"/><circle cx="8" cy="6" r="2" fill="var(--label-cream)"/></svg>
          Unit 4 Market Lane, Hollow Road, Kilbrook, Ireland
        </p>
      </div>
    </div>
  </main>
</body>
</html>
```